Crestline Decor Depot needs Business cards and letterhead

letterhead, envelope & business card
Letterhead:
Crestline Decor Depot
4823 Larkfield Drive Bozeman, MT 59744
Phone #: (406) 555-0148
Fax#: (406) 555-0192
Business cards:
Crestline Decor Depot
Phone #: (406) 555-0148
Fax#: (406) 555-0192
Corinne Vasko
corinne@crestlinedecordepot.example
www.crestlinedecordepot.example
Target Market(s)
Home Interiors client
Industry/Entity Type
Business
Requirements
Must have
- ONLY submit straight front view on white background
- I DO NOT WANT ANY MOCK UPS
Nice to have
- see attached logo use guide
Should not have

```html
<!DOCTYPE html>
<html lang="en">
<head>
<meta charset="utf-8">
<title>Crestline Decor Depot — Business Card</title>
<link href="https://fonts.googleapis.com/css2?family=Poppins:wght@400;500;600;700&display=swap" rel="stylesheet">
<style>
  :root {
    --page: #f2f3f5;
    --card-white: #ffffff;
    --brand-blue: #4fb8ee;
    --deep-blue: #1b72c2;
    --ink: #1d1d1f;
    --muted: #555;
    --on-blue: #ffffff;
  }
  html, body {
    margin: 0;
    width: 1200px;
    height: 934px;
    overflow: hidden;
    background: var(--page);
    font-family: "Poppins", sans-serif;
  }
  .sheet {
    position: relative;
    width: 1200px;
    height: 934px;
  }
  .card {
    position: absolute;
    left: 250px;
    width: 700px;
    height: 400px;
    border-radius: 26px;
    overflow: hidden;
    box-shadow: 0 2px 10px rgba(0,0,0,0.12);
  }
  .card--front { top: 50px; background: var(--card-white); }
  .card--back { top: 484px; background: var(--brand-blue); }
  .card__art { position: absolute; inset: 0; }

  .holder { position: absolute; left: 44px; top: 40px; }
  .holder__name {
    margin: 0;
    font-size: 34px;
    font-weight: 600;
    letter-spacing: 1px;
    color: var(--ink);
    text-transform: uppercase;
    line-height: 1.1;
  }
  .holder__role {
    margin: 4px 0 0;
    font-size: 11px;
    letter-spacing: 1.5px;
    color: var(--muted);
    text-transform: uppercase;
  }

  .brand-name {
    position: absolute;
    font-weight: 600;
    text-transform: uppercase;
    letter-spacing: 1px;
    line-height: 1.15;
    display: flex;
    align-items: center;
    gap: 8px;
  }
  .brand-name__mark {
    width: 12px; height: 12px; flex: none;
    background: currentColor;
  }
  .brand-name--on-blue { left: 32px; top: 246px; color: var(--on-blue); font-size: 17px; }
  .brand-name--on-white { right: 24px; top: 222px; color: var(--deep-blue); font-size: 14px; }
  .brand-name--back { left: 0; right: 0; top: 150px; justify-content: center; color: var(--deep-blue); font-size: 34px; }

  .contact {
    position: absolute;
    left: 205px;
    top: 215px;
    margin: 0;
    padding: 0;
    list-style: none;
    color: var(--on-blue);
    font-size: 14px;
    line-height: 1.35;
  }
  .contact__item { display: flex; align-items: flex-start; gap: 9px; margin-bottom: 6px; white-space: nowrap; }
  .contact__item svg { width: 14px; height: 14px; flex: none; margin-top: 3px; fill: var(--on-blue); }
  .contact__pair { gap: 18px; }
  .contact__pair span { display: flex; gap: 9px; align-items: flex-start; }

  .back-web {
    position: absolute; left: 0; right: 0; top: 232px;
    text-align: center;
    font-size: 20px;
    font-weight: 500;
    letter-spacing: 1.5px;
    color: var(--deep-blue);
    text-transform: uppercase;
  }
</style>
</head>
<body>
<main class="sheet">

  <section class="card card--front" aria-label="Business card front">
    <svg class="card__art" viewBox="0 0 700 400" aria-hidden="true">
      <polygon points="0,150 490,205 570,400 0,400" fill="var(--brand-blue)"/>
      <polygon points="0,140 500,196 584,400 570,400 490,205 0,150" fill="var(--deep-blue)"/>
    </svg>

    <div class="holder">
      <h1 class="holder__name">Corinne Vasko</h1>
      <p class="holder__role">Designation</p>
    </div>

    <div class="brand-name brand-name--on-blue">Crestline<br>Decor Depot</div>

    <ul class="contact">
      <li class="contact__item">
        <svg viewBox="0 0 16 16"><path d="M8 0a5.5 5.5 0 0 0-5.5 5.5C2.5 10 8 16 8 16s5.5-6 5.5-10.5A5.5 5.5 0 0 0 8 0zm0 8a2.5 2.5 0 1 1 0-5 2.5 2.5 0 0 1 0 5z"/></svg>
        <span>4823 Larkfield Drive Bozeman,<br>MT 59744</span>
      </li>
      <li class="contact__item contact__pair">
        <span><svg viewBox="0 0 16 16"><path d="M3.6 0 6 3.8 4.4 5.6a10 10 0 0 0 6 6l1.8-1.6L16 12.4 14.2 15C7 15.6.4 9 1 1.8z"/></svg>(406) 555-0148</span>
        <span><svg viewBox="0 0 16 16"><rect x="1" y="5" width="14" height="10" rx="1.5"/><rect x="4" y="0" width="8" height="6" fill="var(--on-blue)"/></svg>(406) 555-0192</span>
      </li>
      <li class="contact__item">
        <svg viewBox="0 0 16 16"><path d="M0 3h16v1.2L8 9 0 4.2z"/><path d="M0 5.8 8 10.6l8-4.8V13H0z"/></svg>
        <span>corinne@crestlinedecordepot.example</span>
      </li>
      <li class="contact__item">
        <svg viewBox="0 0 16 16"><circle cx="8" cy="8" r="7.2" fill="none" stroke="#fff" stroke-width="1.4"/><ellipse cx="8" cy="8" rx="3" ry="7.2" fill="none" stroke="#fff" stroke-width="1.2"/><path d="M1 8h14" stroke="#fff" stroke-width="1.2"/></svg>
        <span>www.crestlinedecordepot.example</span>
      </li>
    </ul>

    <div class="brand-name brand-name--on-white"><span>Crestline<br>Decor Depot</span><span class="brand-name__mark"></span></div>
  </section>

  <section class="card card--back" aria-label="Business card back">
    <svg class="card__art" viewBox="0 0 700 400" aria-hidden="true">
      <line x1="90" y1="120" x2="610" y2="120" stroke="var(--deep-blue)" stroke-width="1.5"/>
      <line x1="90" y1="290" x2="610" y2="290" stroke="var(--deep-blue)" stroke-width="1.5"/>
      <line x1="150" y1="206" x2="550" y2="206" stroke="var(--deep-blue)" stroke-width="2"/>
    </svg>
    <div class="brand-name brand-name--back">Crestline Decor Depot<span class="brand-name__mark"></span></div>
    <div class="back-web">www.crestlinedecordepot.example</div>
  </section>

</main>
</body>
</html>
```